Harbor Lantern Business Card
remarkable business card
Project: Harbor Lantern Business Card
Harbor Lantern Business Card - Events
Creative Brief
Use specific fonts
Use the fonts in my logo and/or the fonts that look best
Bright & Fun-filled
Tom Vesk
Culture Director
not to be listed on the card
Vesk@HarborLantern.example
www.HarborLantern.example
I want the Name to be prominent . I don't want the address to be listed This should be a very remarkable card. It needs to get instant attention that people will remember, and talk about. People should say wow! you need to see this card. That is a great looking card!

```html
<!DOCTYPE html>
<html lang="en">
<head>
<meta charset="utf-8">
<title>Harbor Lantern Business Card</title>
<link href="https://fonts.googleapis.com/css2?family=Arimo:wght@400;700&display=swap" rel="stylesheet">
<style>
  :root {
    --backdrop: #d8d3cc;
    --card: #ffffff;
    --ink: #3a3a3a;
    --muted: #666666;
    --brand: #5f9a2c;
    --band-dark: #0f63b8;
    --band-light: #3f9be6;
    --band-edge: #9cc9ef;
  }
  * { margin: 0; padding: 0; box-sizing: border-box; }
  html, body { width: 1200px; height: 758px; overflow: hidden; }
  body {
    background: var(--backdrop);
    font-family: "Arimo", Arial, sans-serif;
    color: var(--ink);
    position: relative;
  }
  .card {
    position: absolute;
    background: var(--card);
    box-shadow: 0 6px 14px rgba(0,0,0,0.28);
    overflow: hidden;
  }
  .card--contact { left: 67px; top: 67px; width: 492px; height: 286px; }
  .card--logo { left: 631px; top: 67px; width: 502px; height: 286px; }
  .card--band { left: 350px; top: 403px; width: 495px; height: 288px; }

  .band {
    position: absolute; left: 0; right: 0; bottom: 0; height: 24px;
    background: linear-gradient(180deg, var(--band-light), var(--band-dark));
    border-top: 3px solid var(--band-edge);
    color: #ffffff; font-size: 12px; text-align: center; line-height: 21px;
  }

  .brand { position: absolute; display: flex; align-items: center; gap: 14px; }
  .brand__dot {
    width: 56px; height: 56px; border-radius: 50%;
    background: var(--brand);
  }
  .brand__name { font-size: 36px; font-weight: 700; color: var(--brand); letter-spacing: -0.5px; }

  .card--contact .brand { left: 40px; top: 50px; }
  .card--logo .brand { left: 78px; top: 100px; }
  .card--band .brand { left: 96px; top: 98px; }

  .url-under { position: absolute; left: 148px; top: 168px; font-size: 13px; color: var(--muted); }

  .contact-list { position: absolute; left: 30px; top: 170px; list-style: none; font-size: 13px; color: var(--muted); }
  .contact-list li { display: flex; align-items: center; gap: 7px; height: 18px; }
  .contact-list svg { width: 11px; height: 11px; fill: var(--muted); }

  .person { position: absolute; right: 40px; top: 200px; text-align: left; }
  .person__name { font-size: 20px; color: var(--ink); }
  .person__role { font-size: 13px; color: var(--muted); margin-top: 6px; }
</style>
</head>
<body>

  <section class="card card--contact">
    <div class="brand"><span class="brand__dot"></span><span class="brand__name">Harbor Lantern</span></div>
    <ul class="contact-list">
      <li><svg viewBox="0 0 12 12"><rect x="3" y="0" width="6" height="12" rx="1.5"/></svg>555-204-7381</li>
      <li><svg viewBox="0 0 12 12"><rect x="0" y="3" width="12" height="7" rx="1.5"/><rect x="3" y="1" width="6" height="3"/></svg>555-318-6620</li>
      <li><svg viewBox="0 0 12 12"><circle cx="6" cy="6" r="5.5"/></svg>Vesk@HarborLantern.example</li>
      <li><svg viewBox="0 0 12 12"><circle cx="6" cy="6" r="5" fill="none" stroke="#666" stroke-width="1.5"/><line x1="1" y1="6" x2="11" y2="6" stroke="#666"/></svg>www.HarborLantern.example</li>
    </ul>
    <div class="person">
      <p class="person__name">Tom Vesk</p>
      <p class="person__role">Culture Director</p>
    </div>
    <div class="band"></div>
  </section>

  <section class="card card--logo">
    <div class="brand"><span class="brand__dot"></span><span class="brand__name">Harbor Lantern</span></div>
    <p class="url-under">www.HarborLantern.example</p>
    <div class="band"></div>
  </section>

  <section class="card card--band">
    <div class="brand"><span class="brand__dot"></span><span class="brand__name">Harbor Lantern</span></div>
    <div class="band">www.HarborLantern.example</div>
  </section>

</body>
</html>
```